Business Card for beauty technology startup

Design Glowra Business Card for a Beauty, based on the website identity and colors (https://www.glowra-example.com).
Glowra is a beauty tech startup that gathers helpful product info for beauty lovers and consumers (such as availability on stores, price range and product reviews) for makeup products. The card design must be young, colorful but clean, and very modern.

Target Market(s)

woman, 15-35

Industry/Entity Type

Cosmetics

Contact Information for Business Card

Full Name, address, phone

Font styles to use
Other font styles liked:
• Advent Pro

Colors
e34297
86cfc6
ffffff
5c5c5c
e8e8e8
e667a6
b2b2b2

Requirements
Must have
• One full colored side with a creative design and another with card info
• Use Color palette: #95C5C5 and/or #D38AA5
• Use fonts: Advent Pro
• Use website identity: https://www.glowra-example.com
Nice to have
• If needed extra font: Roboto

```html
<!DOCTYPE html>
<html lang="en">
<head>
<meta charset="utf-8">
<title>Glowra Business Card</title>
<link rel="stylesheet" href="https://fonts.googleapis.com/css2?family=Advent+Pro:wght@400;500;600;700&family=Lato:wght@400;700&display=swap">
<style>
  :root {
    --pink: #e667a6;
    --white: #ffffff;
    --ink: #1e1e1e;
    --grey: #5c5c5c;
    --soft-grey: #e8e8e8;
    --line-grey: #b2b2b2;
  }
  * { margin: 0; padding: 0; box-sizing: border-box; }
  html, body { width: 1200px; height: 926px; overflow: hidden; }
  body {
    background: var(--soft-grey);
    display: flex;
    flex-direction: column;
    align-items: center;
    justify-content: center;
    gap: 42px;
    font-family: "Lato", sans-serif;
  }
  .card {
    position: relative;
    width: 700px;
    height: 400px;
    background: var(--white);
    overflow: hidden;
    box-shadow: 0 6px 18px rgba(0,0,0,0.12);
  }
  .pink-panel {
    position: absolute;
    top: 0; left: 0; bottom: 0;
    background: var(--pink);
  }

  /* Brand side */
  .card-brand .pink-panel { width: 54%; }
  .brand-lockup {
    position: absolute;
    display: flex;
    align-items: center;
    gap: 12px;
    color: #3a2a33;
    font-family: "Advent Pro", sans-serif;
    font-weight: 500;
    font-size: 26px;
    letter-spacing: 4px;
  }
  .brand-dot {
    width: 30px; height: 30px;
    border: 1.5px solid #3a2a33;
    border-radius: 50%;
  }
  .card-brand .brand-lockup { top: 44px; left: 44px; }
  .website {
    position: absolute;
    left: 318px;
    top: 292px;
    display: flex;
    align-items: center;
    gap: 10px;
    font-family: "Advent Pro", sans-serif;
    font-weight: 600;
    font-size: 15px;
    letter-spacing: 4px;
    color: var(--ink);
  }
  .website::before {
    content: "";
    width: 22px;
    height: 2px;
    background: var(--ink);
  }

  /* Info side */
  .card-info .pink-panel { width: 40%; }
  .card-info .brand-lockup {
    left: 70px;
    top: 200px;
    transform-origin: left top;
    transform: rotate(-90deg) translate(-50%, 0);
  }
  .person {
    position: absolute;
    left: 300px;
    top: 60px;
    padding-left: 14px;
    border-left: 3px solid var(--ink);
    font-family: "Advent Pro", sans-serif;
  }
  .person-name {
    font-size: 27px;
    font-weight: 700;
    letter-spacing: 2.5px;
    color: var(--ink);
    line-height: 1;
  }
  .person-title {
    margin-top: 4px;
    font-size: 11px;
    font-weight: 600;
    letter-spacing: 3px;
    color: var(--grey);
  }
  .contact {
    position: absolute;
    left: 320px;
    top: 228px;
    color: var(--grey);
    font-size: 17px;
    list-style: none;
  }
  .contact li {
    display: flex;
    align-items: center;
    gap: 12px;
    height: 24px;
  }
  .contact svg { width: 15px; height: 15px; fill: var(--grey); flex: none; }
  .address {
    position: absolute;
    left: 306px;
    top: 306px;
    color: var(--grey);
    font-size: 17px;
    line-height: 1.45;
  }
</style>
</head>
<body>

<section class="card card-brand">
  <div class="pink-panel"></div>
  <div class="brand-lockup"><span class="brand-dot"></span><span>GLOWRA</span></div>
  <div class="website">WWW.GLOWRA-EXAMPLE.COM</div>
</section>

<section class="card card-info">
  <div class="pink-panel"></div>
  <div class="brand-lockup"><span class="brand-dot"></span><span>GLOWRA</span></div>

  <div class="person">
    <div class="person-name">MAYA LORNE</div>
    <div class="person-title">TITLE GOES HERE</div>
  </div>

  <ul class="contact">
    <li>
      <svg viewBox="0 0 16 16"><path d="M2 5c0-2 2-3 6-3s6 1 6 3v1h-3V4.5H5V6H2z M4 7h8l2 6H2z M8 8.5a2 2 0 1 0 0 4a2 2 0 1 0 0-4z"/></svg>
      <span>555-014-2270</span>
    </li>
    <li>
      <svg viewBox="0 0 16 16"><path d="M6.5 9.5l3-3M7 4.5l1.5-1.5a2.5 2.5 0 0 1 3.5 3.5L10.5 8M9 11.5L7.5 13a2.5 2.5 0 0 1-3.5-3.5L5.5 8" stroke="#5c5c5c" stroke-width="1.8" fill="none" stroke-linecap="round"/></svg>
      <span>www.glowra-example.com</span>
    </li>
    <li>
      <svg viewBox="0 0 16 16"><path d="M1 3.5h14v9H1z M1.5 4l6.5 5 6.5-5" stroke="#5c5c5c" stroke-width="1.3" fill="none"/></svg>
      <span>hello@glowra-example.com</span>
    </li>
  </ul>

  <address class="address" style="font-style:normal">
    Street address goes here,<br>
    Suite #210, Lark Bldg, NY 10488
  </address>
</section>

</body>
</html>
```